Tall Maple Hydration Product that supports healthy blood pressure and Hydration

Design Brief: Hydration Product for Blood Pressure Support
Product Name: "42" or "Halvia"
We are developing a hydration product aimed at supporting healthy blood pressure while keeping users hydrated. The product will have a clinical, clean, and functional design, and we're looking for a professional designer or team to bring this vision to life.

Project Overview
We want a product design (logo, label, and possibly packaging) that communicates:

Hydration

Blood pressure support

Pharmaceutical/medical Look

Health and wellness

This product will be used by health-conscious consumers and individuals managing their blood pressure.

Design Objectives
Reflect both hydration and blood pressure support visually.

Appeal to a clinical, trustworthy, yet fresh and modern aesthetic.

Clearly communicate functionality and health benefits.

Visual Elements to Consider
We would like to explore the use of the following visual motifs:

Water drop – to symbolize hydration

Blood drop – to signify blood pressure support

Medical or pharmaceutical elements – cross, heartbeat/EKG lines, capsules, etc.

Typography – Clean, sans-serif fonts; professional and modern

Color Preferences
We have attached reference images showing preferred color schemes. These are mostly in the blue, red, and white family (for hydration, blood, and clinical cleanliness).

However, we are open to other colors that you feel will enhance the brand’s purpose.

Target Market(s)

Hydration

Industry/Entity Type

Health and Wellness

Font styles to use
Serif
Sans Serif
Decorative
Script

Colors
00AB8E
00BBA5
67D7C9
C6EFE9
E9F9F6

Requirements
Must have
• design that incorporates a clean pharmaceutical look and refreshing design
Nice to have
• Medica look
Should not have
• Clean Design. Silver and Cobalt Blue Design as an additional

```html
<!DOCTYPE html>
<html lang="en">
<head>
<meta charset="utf-8">
<title>Halvia – Hydration + Blood Pressure Support</title>
<link rel="stylesheet" href="https://fonts.googleapis.com/css2?family=Source+Sans+3:wght@600;700&display=swap">
<style>
  :root {
    --backdrop: #ebe8e4;
    --pack-white: #f4f5f6;
    --crimp-silver: #d9dadc;
    --crimp-line: #c3c5c8;
    --navy: #0d2a52;
    --aqua: #2ea3d3;
    --sea: #1b86c4;
    --cobalt: #0f55a6;
    --cobalt-deep: #0a3f8c;
    --lime: #d6f51c;
    --mark-blue: #12a0dc;
    --white: #ffffff;
  }
  * { margin: 0; padding: 0; box-sizing: border-box; }
  html, body {
    width: 1200px;
    height: 2227px;
    overflow: hidden;
    background: var(--backdrop);
  }
  .canvas {
    position: relative;
    width: 1200px;
    height: 2227px;
    font-family: "Source Sans 3", sans-serif;
  }
  .pack-art {
    position: absolute;
    inset: 0;
  }
  .label-text {
    position: absolute;
    left: 300px;
    width: 600px;
    text-align: center;
  }
  .brand-name {
    top: 390px;
    font-size: 166px;
    font-weight: 700;
    letter-spacing: 1px;
    line-height: 1;
    color: var(--navy);
  }
  .benefit {
    top: 978px;
    font-size: 61px;
    font-weight: 600;
    line-height: 78px;
    color: var(--navy);
  }
  .flavor {
    top: 1436px;
    font-size: 74px;
    font-weight: 600;
    line-height: 1;
    color: var(--lime);
  }
  .directions {
    top: 1560px;
    font-size: 40px;
    font-weight: 700;
    line-height: 55px;
    color: var(--white);
  }
  .net-weight {
    top: 1920px;
    font-size: 40px;
    font-weight: 700;
    line-height: 1;
    color: var(--white);
  }
</style>
</head>
<body>
<main class="canvas">
  <svg class="pack-art" width="1200" height="2227" viewBox="0 0 1200 2227" aria-hidden="true">
    <defs>
      <clipPath id="pack-body">
        <rect x="300" y="84" width="600" height="2068" rx="10"/>
      </clipPath>
    </defs>
    <g clip-path="url(#pack-body)">
      <rect class="pack-base" x="300" y="84" width="600" height="2068" fill="var(--pack-white)"/>
      <path class="wave-aqua" d="M300 1183 C420 1240 560 1320 700 1296 C790 1280 860 1250 900 1226 L900 2152 L300 2152 Z" fill="var(--aqua)"/>
      <path class="wave-sea" d="M300 1560 C480 1520 700 1480 900 1400 L900 2152 L300 2152 Z" fill="var(--sea)" opacity="0.55"/>
      <path class="wave-cobalt" d="M300 1850 C500 1830 720 1790 900 1720 L900 2152 L300 2152 Z" fill="var(--cobalt)"/>
      <path class="wave-cobalt-deep" d="M300 2000 C520 1985 720 1970 900 1940 L900 2152 L300 2152 Z" fill="var(--cobalt-deep)"/>
      <g class="seal-top">
        <rect x="300" y="84" width="600" height="62" fill="var(--crimp-silver)"/>
        <path d="M300 96 H900 M300 106 H900 M300 116 H900 M300 126 H900 M300 136 H900" stroke="var(--crimp-line)" stroke-width="3"/>
      </g>
      <g class="seal-bottom">
        <rect x="300" y="2090" width="600" height="62" fill="var(--cobalt-deep)"/>
        <path d="M300 2100 H900 M300 2110 H900 M300 2120 H900 M300 2130 H900 M300 2140 H900" stroke="var(--cobalt)" stroke-width="3"/>
      </g>
    </g>
    <circle class="brand-dot" cx="600" cy="754" r="114" fill="var(--mark-blue)"/>
  </svg>

  <h1 class="label-text brand-name">HALVIA</h1>
  <p class="label-text benefit">HYDRATION +<br>BLOOD PRESSURE<br>SUPPORT</p>
  <p class="label-text flavor">LEMON LIME</p>
  <p class="label-text directions">ADD TO 16 Oz<br>(500mL) OF WATER</p>
  <p class="label-text net-weight">NET WT 0.56 Oz (16g)</p>
</main>
</body>
</html>
```